Banners for Website and Social Media

Technology Consulting and Services company requires several banners that integrate our logo that can be used on a basic website that we are designing. The design will also be used on social media platforms. Require a variety of sizes and shapes to be included. Need at least two variations for a website header, more variations will put you at the top of the leaderboard.

Target Market(s)

Non-Profit Mental Health Agencies, small business

Font styles to use
Serif

Requirements
Must have
• Show the idea of connecting with our clients. We require the following approximate sizes, they do not have to be exact:

2 x variations 1080px x 600px for website header
1 x 1128px x 191px for Brindlepost
1 x 590px x 175px for Email Marketing
1 x 300px x 250px for Advertising

Colours should compliment the logo that has been provided.
Nice to have
• Could integrate key words and phrases in the graphic but not standout as a tagline or title.

- Engaged
- Ethical Technology
- Support
- Connected
Should not have
• Banner should avoid having people in it. Prefer a more abstract feel.

```html
<!DOCTYPE html>
<html lang="en">
<head>
<meta charset="utf-8">
<title>Harbourline Systems Advisors – Banner Set</title>
<link rel="stylesheet" href="https://fonts.googleapis.com/css2?family=Saira+Condensed:wght@400;600&display=swap">
<style>
  :root {
    --page: #ffffff;
    --navy-deep: #050d1c;
    --navy: #0b2440;
    --steel: #134a6e;
    --panel: #114673;
    --panel-dark: #0c3558;
    --teal: #3e8e8a;
    --glow: #cfe9ff;
    --text: #ffffff;
  }
  html, body {
    margin: 0;
    width: 1200px;
    height: 1200px;
    overflow: hidden;
    background: var(--page);
    font-family: "Saira Condensed", "Arial Narrow", sans-serif;
    color: var(--text);
  }
  .canvas { position: relative; width: 1200px; height: 1200px; }
  .banner {
    position: absolute;
    overflow: hidden;
    box-shadow: 6px 8px 8px rgba(0,0,0,0.35);
  }
  .banner > svg.backdrop { position: absolute; inset: 0; width: 100%; height: 100%; display: block; }
  .brand { position: absolute; display: flex; align-items: center; gap: 10px; }
  .brand-dot {
    border: 3px solid var(--text);
    border-radius: 50%;
    box-sizing: border-box;
    flex: none;
  }
  .brand-name {
    font-weight: 600;
    letter-spacing: 0.02em;
    text-transform: uppercase;
    white-space: nowrap;
    line-height: 1;
  }
  .brand.stacked { flex-direction: column; gap: 8px; }
  .values { position: absolute; margin: 0; padding: 0; list-style: none; }
  .values li { display: flex; align-items: center; line-height: 1; white-space: nowrap; font-weight: 400; }
  .values svg { flex: none; }
  .values.grid { display: grid; grid-template-columns: auto auto; column-gap: 22px; row-gap: 10px; }
  .values.row { display: flex; gap: 22px; }

  .header-a { left: 72px; top: 231px; width: 553px; height: 308px; }
  .header-a .brand { left: 18px; top: 10px; width: 170px; }
  .header-a .brand-dot { width: 68px; height: 68px; }
  .header-a .brand-name { font-size: 15px; }
  .header-a .values { left: 18px; top: 146px; }
  .header-a .values li { font-size: 28px; gap: 20px; height: 39px; }

  .email { left: 72px; top: 595px; width: 559px; height: 165px; }
  .email .brand { left: 10px; top: 16px; }
  .email .brand-dot { width: 50px; height: 50px; }
  .email .brand-name { font-size: 17px; }
  .email .values { left: 10px; top: 99px; }
  .email .values li { font-size: 20px; gap: 7px; }

  .advert { left: 672px; top: 376px; width: 462px; height: 384px; }
  .advert .brand { left: 0; right: 0; top: 17px; }
  .advert .brand-dot { width: 78px; height: 78px; }
  .advert .brand-name { font-size: 18px; }
  .advert .values { left: 26px; top: 198px; }
  .advert .values li { font-size: 30px; gap: 22px; height: 44px; }

  .profile { left: 72px; top: 807px; width: 1060px; height: 179px; }
  .profile .brand { left: 28px; top: 12px; }
  .profile .brand-dot { width: 68px; height: 68px; }
  .profile .brand-name { font-size: 22px; }
  .profile .values { left: 26px; top: 131px; }
  .profile .values li { font-size: 22px; gap: 6px; }
</style>
</head>
<body>
<main class="canvas">

  <!-- Website header -->
  <section class="banner header-a">
    <svg class="backdrop" viewBox="0 0 553 308" preserveAspectRatio="none">
      <defs>
        <linearGradient id="bgA" x1="0" x2="1" y1="0" y2="0">
          <stop offset="0" stop-color="#0a0f1c"/><stop offset="0.45" stop-color="#0b2440"/><stop offset="1" stop-color="#12405f"/>
        </linearGradient>
        <radialGradient id="glowA" cx="0.67" cy="0.73" r="0.55">
          <stop offset="0" stop-color="#cfe9ff" stop-opacity="0.9"/><stop offset="0.12" stop-color="#5fa6d4" stop-opacity="0.55"/><stop offset="1" stop-color="#134a6e" stop-opacity="0"/>
        </radialGradient>
      </defs>
      <g role="img" aria-label="Abstract glowing network of connected nodes">
        <rect width="553" height="308" fill="url(#bgA)"/>
        <rect width="553" height="308" fill="url(#glowA)"/>
      </g>
      <path d="M0,124 Q190,112 265,165 Q305,200 300,308 L0,308 Z" fill="var(--teal)" opacity="0.8"/>
      <path d="M0,132 Q185,118 255,170 Q290,205 275,308 L0,308 Z" fill="var(--panel)"/>
    </svg>
    <div class="brand stacked"><span class="brand-dot"></span><span class="brand-name">Harbourline Systems</span></div>
    <ul class="values">
      <li><svg width="20" height="20" viewBox="0 0 20 20"><path d="M17 8A7.5 7.5 0 1 1 13 3.3" fill="none" stroke="#fff" stroke-width="2"/><path d="M6 10l3 3 7-7" fill="none" stroke="#fff" stroke-width="2"/></svg>Engaged</li>
      <li><svg width="20" height="20" viewBox="0 0 20 20"><path d="M17 8A7.5 7.5 0 1 1 13 3.3" fill="none" stroke="#fff" stroke-width="2"/><path d="M6 10l3 3 7-7" fill="none" stroke="#fff" stroke-width="2"/></svg>Ethical Technology</li>
      <li><svg width="20" height="20" viewBox="0 0 20 20"><path d="M17 8A7.5 7.5 0 1 1 13 3.3" fill="none" stroke="#fff" stroke-width="2"/><path d="M6 10l3 3 7-7" fill="none" stroke="#fff" stroke-width="2"/></svg>Support</li>
      <li><svg width="20" height="20" viewBox="0 0 20 20"><path d="M17 8A7.5 7.5 0 1 1 13 3.3" fill="none" stroke="#fff" stroke-width="2"/><path d="M6 10l3 3 7-7" fill="none" stroke="#fff" stroke-width="2"/></svg>Connected</li>
    </ul>
  </section>

  <!-- Email marketing -->
  <section class="banner email">
    <svg class="backdrop" viewBox="0 0 559 165" preserveAspectRatio="none">
      <defs>
        <linearGradient id="bgB" x1="0" x2="1"><stop offset="0" stop-color="#0a0f1c"/><stop offset="0.5" stop-color="#0b2440"/><stop offset="1" stop-color="#134a6e"/></linearGradient>
        <radialGradient id="glowB" cx="0.76" cy="0.55" r="0.4"><stop offset="0" stop-color="#cfe9ff" stop-opacity="0.9"/><stop offset="0.15" stop-color="#5fa6d4" stop-opacity="0.5"/><stop offset="1" stop-color="#134a6e" stop-opacity="0"/></radialGradient>
      </defs>
      <g role="img" aria-label="Abstract glowing network of connected nodes">
        <rect width="559" height="165" fill="url(#bgB)"/>
        <rect width="559" height="165" fill="url(#glowB)"/>
      </g>
      <path d="M0,76 Q240,66 330,100 Q365,120 375,165 L0,165 Z" fill="var(--teal)" opacity="0.8"/>
      <path d="M0,84 Q235,72 320,104 Q350,125 362,165 L0,165 Z" fill="var(--panel)"/>
    </svg>
    <div class="brand"><span class="brand-dot"></span><span class="brand-name">Harbourline Systems</span></div>
    <ul class="values grid">
      <li><svg width="15" height="15" viewBox="0 0 20 20"><path d="M17 8A7.5 7.5 0 1 1 13 3.3" fill="none" stroke="#fff" stroke-width="2"/><path d="M6 10l3 3 7-7" fill="none" stroke="#fff" stroke-width="2"/></svg>Engaged</li>
      <li><svg width="15" height="15" viewBox="0 0 20 20"><path d="M17 8A7.5 7.5 0 1 1 13 3.3" fill="none" stroke="#fff" stroke-width="2"/><path d="M6 10l3 3 7-7" fill="none" stroke="#fff" stroke-width="2"/></svg>Ethical Technology</li>
      <li><svg width="15" height="15" viewBox="0 0 20 20"><path d="M17 8A7.5 7.5 0 1 1 13 3.3" fill="none" stroke="#fff" stroke-width="2"/><path d="M6 10l3 3 7-7" fill="none" stroke="#fff" stroke-width="2"/></svg>Support</li>
      <li><svg width="15" height="15" viewBox="0 0 20 20"><path d="M17 8A7.5 7.5 0 1 1 13 3.3" fill="none" stroke="#fff" stroke-width="2"/><path d="M6 10l3 3 7-7" fill="none" stroke="#fff" stroke-width="2"/></svg>Connected</li>
    </ul>
  </section>

  <!-- Advertising -->
  <section class="banner advert">
    <svg class="backdrop" viewBox="0 0 462 384" preserveAspectRatio="none">
      <defs>
        <linearGradient id="bgC" x1="0" x2="1"><stop offset="0" stop-color="#07142a"/><stop offset="0.5" stop-color="#0b2440"/><stop offset="1" stop-color="#134a6e"/></linearGradient>
        <radialGradient id="glowC" cx="0.78" cy="0.47" r="0.45"><stop offset="0" stop-color="#cfe9ff" stop-opacity="0.9"/><stop offset="0.15" stop-color="#5fa6d4" stop-opacity="0.5"/><stop offset="1" stop-color="#134a6e" stop-opacity="0"/></radialGradient>
      </defs>
      <g role="img" aria-label="Abstract glowing network of connected nodes">
        <rect width="462" height="384" fill="url(#bgC)"/>
        <rect width="462" height="384" fill="url(#glowC)"/>
      </g>
      <path d="M0,160 Q210,148 285,200 Q335,240 337,384 L0,384 Z" fill="var(--teal)" opacity="0.8"/>
      <path d="M0,168 Q205,155 275,205 Q320,245 322,384 L0,384 Z" fill="var(--panel)"/>
    </svg>
    <div class="brand stacked"><span class="brand-dot"></span><span class="brand-name">Harbourline Systems</span></div>
    <ul class="values">
      <li><svg width="22" height="22" viewBox="0 0 20 20"><path d="M17 8A7.5 7.5 0 1 1 13 3.3" fill="none" stroke="#fff" stroke-width="2"/><path d="M6 10l3 3 7-7" fill="none" stroke="#fff" stroke-width="2"/></svg>Engaged</li>
      <li><svg width="22" height="22" viewBox="0 0 20 20"><path d="M17 8A7.5 7.5 0 1 1 13 3.3" fill="none" stroke="#fff" stroke-width="2"/><path d="M6 10l3 3 7-7" fill="none" stroke="#fff" stroke-width="2"/></svg>Ethical Technology</li>
      <li><svg width="22" height="22" viewBox="0 0 20 20"><path d="M17 8A7.5 7.5 0 1 1 13 3.3" fill="none" stroke="#fff" stroke-width="2"/><path d="M6 10l3 3 7-7" fill="none" stroke="#fff" stroke-width="2"/></svg>Support</li>
      <li><svg width="22" height="22" viewBox="0 0 20 20"><path d="M17 8A7.5 7.5 0 1 1 13 3.3" fill="none" stroke="#fff" stroke-width="2"/><path d="M6 10l3 3 7-7" fill="none" stroke="#fff" stroke-width="2"/></svg>Connected</li>
    </ul>
  </section>

  <!-- Professional network profile banner -->
  <section class="banner profile">
    <svg class="backdrop" viewBox="0 0 1060 179" preserveAspectRatio="none">
      <defs>
        <linearGradient id="bgD" x1="0" x2="1"><stop offset="0" stop-color="#07142a"/><stop offset="0.45" stop-color="#0b2440"/><stop offset="1" stop-color="#134a6e"/></linearGradient>
        <radialGradient id="glowD" cx="0.72" cy="0.35" r="0.3"><stop offset="0" stop-color="#e6f4ff" stop-opacity="0.95"/><stop offset="0.15" stop-color="#5fa6d4" stop-opacity="0.5"/><stop offset="1" stop-color="#134a6e" stop-opacity="0"/></radialGradient>
      </defs>
      <g role="img" aria-label="Abstract glowing network of connected nodes">
        <rect width="1060" height="179" fill="url(#bgD)"/>
        <rect width="1060" height="179" fill="url(#glowD)"/>
      </g>
      <path d="M0,94 Q420,80 540,118 Q585,138 600,179 L0,179 Z" fill="var(--teal)" opacity="0.8"/>
      <path d="M0,102 Q410,88 525,122 Q565,142 580,179 L0,179 Z" fill="var(--panel)"/>
    </svg>
    <div class="brand"><span class="brand-dot"></span><span class="brand-name">Harbourline Systems</span></div>
    <ul class="values row">
      <li><svg width="9" height="9" viewBox="0 0 20 20"><path d="M17 8A7.5 7.5 0 1 1 13 3.3" fill="none" stroke="#fff" stroke-width="2.5"/><path d="M6 10l3 3 7-7" fill="none" stroke="#fff" stroke-width="2.5"/></svg>Engaged</li>
      <li><svg width="9" height="9" viewBox="0 0 20 20"><path d="M17 8A7.5 7.5 0 1 1 13 3.3" fill="none" stroke="#fff" stroke-width="2.5"/><path d="M6 10l3 3 7-7" fill="none" stroke="#fff" stroke-width="2.5"/></svg>Ethical Technology</li>
      <li><svg width="9" height="9" viewBox="0 0 20 20"><path d="M17 8A7.5 7.5 0 1 1 13 3.3" fill="none" stroke="#fff" stroke-width="2.5"/><path d="M6 10l3 3 7-7" fill="none" stroke="#fff" stroke-width="2.5"/></svg>Support</li>
      <li><svg width="9" height="9" viewBox="0 0 20 20"><path d="M17 8A7.5 7.5 0 1 1 13 3.3" fill="none" stroke="#fff" stroke-width="2.5"/><path d="M6 10l3 3 7-7" fill="none" stroke="#fff" stroke-width="2.5"/></svg>Connected</li>
    </ul>
  </section>

</main>
</body>
</html>
```